Webdesign für IT Service Firma
Zielgruppe
Wir sind eine IT-Service Firma und bieten individuelle IT-Lösungen. Unsere Kunden sind KMU, also Firmen mit einer Grösse von 2-250 Mitarbeitern im Grossraum Basel, die in Ihrem Bereich Spezialisten sind und spezielle Anforderungen an Ihre IT besitzen.
Unsere USP sind fixe Ansprechpartner, gute Erreichbarkeit, schneller und individueller Service
Aufgabenstellung
Schriftart Myriad Pro
Grün: #7FA51D
Blau: #4D9BC2
Grau: #999999
Untertitel: Wir sind da.

```html
<!DOCTYPE html>
<html lang="de">
<head>
<meta charset="utf-8">
<title>NEVORA – IT Services aus Basel</title>
<link href="https://fonts.googleapis.com/css2?family=Work+Sans:wght@400;500;700;800&display=swap" rel="stylesheet">
<style>
:root{
  --blue:#4d9bc2;
  --blue-dark:#336a88;
  --green:#7fa51d;
  --grey:#999999;
  --ink:#1d2228;
  --footer:#8499ad;
  --page:#f3f6f9;
}
*{margin:0;padding:0;box-sizing:border-box}
html,body{width:971px;height:1200px;overflow:hidden}
body{font-family:"Work Sans",sans-serif;color:var(--ink);background:linear-gradient(180deg,#eef2f6 0%,#f7f9fb 30%,#fff 60%);position:relative}
.abs{position:absolute}
a{color:inherit;text-decoration:none}

.topbar-item{top:17px;display:flex;align-items:center;gap:10px;color:var(--green);font-size:12px}
.lang{top:17px;font-size:7.5px;font-weight:700;color:var(--grey)}
.lang.active{color:var(--blue);background:#f0f4f7;border-radius:50%;width:22px;height:22px;display:flex;align-items:center;justify-content:center;top:14px}

.header{left:164px;top:52px;width:642px;height:98px;background:#fff;border-radius:6px 6px 0 0;overflow:hidden;box-shadow:0 2px 10px rgba(0,0,0,.04)}
.brand{position:absolute;left:25px;top:14px;font-size:32px;font-weight:400;color:var(--blue);letter-spacing:1px;display:flex;align-items:center;gap:8px}
.brand .dot{width:9px;height:9px;background:var(--green)}
.tagline{position:absolute;left:363px;top:27px;font-size:11.5px;color:var(--blue)}
.skyline{position:absolute;right:0;top:0;width:150px;height:63px;background:linear-gradient(90deg,rgba(77,155,194,0) 0%,rgba(77,155,194,.35) 60%,rgba(77,155,194,.55) 100%)}
.nav{position:absolute;left:0;top:63px;width:100%;height:35px;background:var(--blue);display:flex;align-items:center;gap:14px;padding-left:23px}
.nav a{color:#fff;font-weight:700;font-size:11.5px}

.hero-photo{left:60px;top:150px;width:520px;height:330px;background:radial-gradient(ellipse at 45% 45%,#8fa9bd 0%,#b8cad8 40%,rgba(230,237,243,0) 72%)}
.hero-text{left:469px;top:216px;font-size:18.5px;line-height:26px}
.hero-text b,.lead b{color:var(--blue);font-weight:700}
.btn{background:var(--blue);color:#fff;display:flex;align-items:center;justify-content:center;font-size:12px;letter-spacing:.3px}

.card{top:423px;width:187px;height:223px;color:#fff;overflow:hidden}
.card .photo{position:absolute;left:0;top:0;width:100%;height:96px;clip-path:polygon(0 0,100% 0,100% 78%,0 100%)}
.card .icon{position:absolute;right:15px;top:90px}
.card h2{position:absolute;left:22px;top:122px;font-size:18px;font-weight:800}
.card p{position:absolute;left:21px;font-size:8.8px;line-height:13px;width:130px}
.card .arrow{position:absolute;right:24px;bottom:15px}

.lead{top:718px;left:150px;width:198px;text-align:right;font-size:12.3px;line-height:17.6px}
.support-photo{left:385px;top:650px;width:450px;height:292px;background:radial-gradient(ellipse at 50% 50%,#9fb0c0 0%,#c5d1dc 45%,rgba(255,255,255,0) 75%)}

.footer{left:0;top:949px;width:971px;height:198px;background:var(--footer);color:#fff}
.contact{position:absolute;left:177px;display:flex;gap:14px;font-size:8.8px;line-height:13px}
.contact .icon{width:20px}
.services-head{position:absolute;left:392px;top:42px;font-size:8.8px;font-weight:700;letter-spacing:.3px}
.svc{position:absolute;font-size:9px;display:flex;align-items:center;gap:6px}
.legal{left:0;top:1147px;width:971px;height:53px;background:#fff}
.legal .brand-small{position:absolute;left:190px;top:16px;font-size:16px;color:var(--blue);display:flex;align-items:center;gap:5px}
.legal .brand-small .dot{width:6px;height:6px;background:var(--green)}
.legal nav{position:absolute;right:171px;top:21px;display:flex;gap:12px;font-size:9px;color:var(--blue)}
</style>
</head>
<body>

<div class="abs topbar-item" style="left:190px">
  <svg width="14" height="14" viewBox="0 0 24 24" fill="none" stroke="#4d9bc2" stroke-width="1.6"><path d="M5 3h4l2 5-2.5 1.5a11 11 0 0 0 6 6L16 13l5 2v4a2 2 0 0 1-2 2A17 17 0 0 1 3 5a2 2 0 0 1 2-2z"/></svg>
  <span>+41 61 000 4821</span>
</div>
<div class="abs topbar-item" style="left:329px">
  <svg width="15" height="11" viewBox="0 0 24 17" fill="none" stroke="#4d9bc2" stroke-width="1.6"><rect x="1" y="1" width="22" height="15" rx="1"/><path d="M1 2l11 8 11-8"/></svg>
  <span>support@nevora.ch</span>
</div>
<span class="abs lang active" style="left:738px">DE</span>
<span class="abs lang" style="left:775px">EN</span>

<header class="abs header">
  <div class="brand"><span>NEVORA</span><span class="dot"></span></div>
  <div class="tagline">IT Services aus Basel</div>
  <div class="skyline" role="img" aria-label="Illustration: Basler Stadtsilhouette mit Leiterbahnen"></div>
  <nav class="nav">
    <a href="#">Home</a><a href="#">Leistungen</a><a href="#">Privatkunde?</a><a href="#">Jobs</a><a href="#">Hilfe</a><a href="#">Sozialprozent</a><a href="#">Über uns</a><a href="#">Kontakt</a>
  </nav>
</header>

<div class="abs hero-photo" role="img" aria-label="Foto: Mitarbeiter arbeitet an einem Computer mit mehreren Bildschirmen"></div>
<p class="abs hero-text">Wir kümmern uns um <b>Ihre IT</b>,<br>damit Sie sich auf Ihr Kerngeschäft<br>konzentrieren können.</p>
<a href="#" class="abs btn" style="left:645px;top:324px;width:132px;height:37px">Mehr erfahren</a>

<article class="abs card" style="left:164px;background:var(--blue-dark)">
  <div class="photo" role="img" aria-label="Illustration: digitale Schlösser auf einer Platine" style="background:linear-gradient(135deg,#0c2a4a,#1d5680)"></div>
  <svg class="icon" width="34" height="34" viewBox="0 0 34 34" fill="none" stroke="#fff" stroke-width="1.2"><rect x="1" y="2" width="32" height="24"/><path d="M1 7h32M5 11h8v5H5zM16 12h8"/><rect x="12" y="22" width="10" height="9"/><path d="M14 22v-3a3 3 0 0 1 6 0v3"/></svg>
  <h2>Sicherheit</h2>
  <p style="top:146px">Wir bieten ganzheitliche IT-Security Lösungen für Ihr Unternehmen!</p>
  <svg class="arrow" width="14" height="12" viewBox="0 0 14 12" fill="none" stroke="#fff" stroke-width="1.6"><path d="M1 6h12M8 1l5 5-5 5"/></svg>
</article>

<article class="abs card" style="left:392px;background:var(--green)">
  <div class="photo" role="img" aria-label="Foto: Techniker mit Laptop im Serverraum" style="background:linear-gradient(135deg,#132a44,#2b4b6a)"></div>
  <svg class="icon" width="34" height="34" viewBox="0 0 34 34" fill="none" stroke="#fff" stroke-width="1.2"><circle cx="17" cy="13" r="11"/><ellipse cx="17" cy="13" rx="5" ry="11"/><path d="M6 13h22M8 7h18M8 19h18M17 24v5M3 30h28"/><circle cx="10" cy="30" r="1.5"/><circle cx="17" cy="30" r="1.5"/><circle cx="24" cy="30" r="1.5"/></svg>
  <h2>Betreuung</h2>
  <p style="top:146px">Wir bieten IT als massgeschneiderte Dienstleistung.</p>
  <svg class="arrow" width="14" height="12" viewBox="0 0 14 12" fill="none" stroke="#fff" stroke-width="1.6"><path d="M1 6h12M8 1l5 5-5 5"/></svg>
</article>

<article class="abs card" style="left:619px;background:var(--blue)">
  <div class="photo" role="img" aria-label="Foto: Support-Team mit Headsets an Bildschirmen" style="background:linear-gradient(135deg,#1b3552,#3c6286)"></div>
  <svg class="icon" width="30" height="34" viewBox="0 0 30 34" fill="none" stroke="#fff" stroke-width="1.2"><circle cx="15" cy="12" r="8"/><path d="M6 13v-2a9 9 0 0 1 18 0v2M6 11h2v5H6zM22 11h2v5h-2zM23 16c0 3-3 5-6 5"/><path d="M3 33c0-6 5-10 12-10s12 4 12 10M11 24l4 5 4-5"/></svg>
  <h2>Support</h2>
  <p style="top:154px">Vertrauen Sie uns, wir kümmern uns um Sie!</p>
  <svg class="arrow" width="14" height="12" viewBox="0 0 14 12" fill="none" stroke="#fff" stroke-width="1.6"><path d="M1 6h12M8 1l5 5-5 5"/></svg>
</article>

<p class="abs lead">Sie benötigen <b>eine stabile IT</b>, damit Sie sich sich voll auf ihr Kerngeschäft konzentrieren können?</p>
<a href="#" class="abs btn" style="left:171px;top:819px;width:187px;height:37px">Kontaktieren Sie uns jetzt</a>
<div class="abs support-photo" role="img" aria-label="Foto: Kundendienst-Mitarbeiter mit Headset am Computer im Grossraumbüro"></div>

<footer class="abs footer">
  <div class="contact" style="top:43px">
    <svg class="icon" width="20" height="24" viewBox="0 0 20 24" fill="none" stroke="#fff" stroke-width="1.6"><path d="M10 23s8-8 8-13a8 8 0 0 0-16 0c0 5 8 13 8 13z"/><circle cx="10" cy="10" r="3"/></svg>
    <div><b>NEVORA GmbH</b><br>Lindenweg 12<br>CH-4000 Basel</div>
  </div>
  <div class="contact" style="top:94px">
    <svg class="icon" width="20" height="20" viewBox="0 0 24 24" fill="none" stroke="#fff" stroke-width="1.6"><path d="M5 3h4l2 5-2.5 1.5a11 11 0 0 0 6 6L16 13l5 2v4a2 2 0 0 1-2 2A17 17 0 0 1 3 5a2 2 0 0 1 2-2z"/></svg>
    <div>Telefon<br>+41 61 000 4821</div>
  </div>
  <div class="contact" style="top:134px">
    <svg class="icon" width="20" height="16" viewBox="0 0 24 18" fill="none" stroke="#fff" stroke-width="1.8"><rect x="1" y="1" width="22" height="16"/><path d="M1 2l11 9 11-9"/></svg>
    <div>Email<br>support@nevora.ch</div>
  </div>

  <div class="services-head">LEISTUNGEN</div>
  <div class="svc" style="left:394px;top:70px">›&nbsp;IT-Betreuung</div>
  <div class="svc" style="left:394px;top:90px">›&nbsp;IT-Sicherheit</div>
  <div class="svc" style="left:394px;top:110px">›&nbsp;Backup</div>
  <div class="svc" style="left:394px;top:131px">›&nbsp;Scientific IT</div>
  <div class="svc" style="left:496px;top:70px">›&nbsp;Websites</div>
  <div class="svc" style="left:496px;top:90px">›&nbsp;Bookline</div>
  <div class="svc" style="left:496px;top:110px">›&nbsp;Coworking Space / Sitzungszimmer</div>
  <div class="svc" style="left:496px;top:130px">›&nbsp;Home Office Lösungen</div>
  <div class="svc" style="left:692px;top:70px">›&nbsp;Telefonie</div>
  <div class="svc" style="left:692px;top:90px">›&nbsp;Monitoring</div>
  <div class="svc" style="left:692px;top:110px">›&nbsp;Passwort Manager</div>
</footer>

<div class="abs legal">
  <div class="brand-small"><span>NEVORA</span><span class="dot"></span></div>
  <nav><a href="#">Newsletter</a><a href="#">Datenschutz</a><a href="#">AGB</a><a href="#">Impressum</a></nav>
</div>

</body>
</html>
```